Save The Date for 2019 RLX Colloquium

We have an annual meeting each June and need a Save the Date (STD) designed. It should be a two-sided postcard with room for address and stamp (according to US Mail postal standards). I have attached some examples from prior years, but we would appreciate a more modern and attractive design for this year's STD.

Target Market(s)

Our own members - nurses, nurse practitioners, PAs and physicians

Industry/Entity Type

Medical

Requirements
Must have
• Must include our logos (attached), ideally in a coordinating fashion - as was done in prior years (see examples attached) and without modifying the logos too much. Needs have the following information:
• - "Save the Date"
• - "The 12th Annual Heartline Crew Colloquium"
• - "Friday, June 7, 2019" or "6/7/19"
• - "The Varrick–Dunmore Building | 318 West 57th Street | NYC"
• - Please include our website (www.qb-zrh.org/events), phone number (212-555-0147) and email address (ask@qb-zrh.org) for people to ask questions
• - Must have space for a postage stamp and the name/address of the postcard recipient
Nice to have
• Would be nice to remain in our blue/grey/olive color palate (see attached Brand Standards guide).
Should not have
• Please do not use stock photos of medical staff. Please don't use cartoons or cartoon images (although a tasteful sketch may be considered).

```html
<!DOCTYPE html>
<html lang="en">
<head>
<meta charset="utf-8">
<title>Save the Date – 2019 RLX Colloquium</title>
<link rel="stylesheet" href="https://fonts.googleapis.com/css2?family=Cinzel:wght@700;900&family=Arimo:wght@400;700&family=Gelasio:wght@400;600&display=swap">
<style>
  :root {
    --backdrop: #364534;
    --royal: #0a4fa8;
    --deep: #0b3a80;
    --sky: #46aee6;
    --ice: #dfeaf5;
    --navy: #1c2f5c;
    --white: #ffffff;
    --stamp: #f5f9e8;
    --dot: #1a2440;
  }
  * { box-sizing: border-box; margin: 0; padding: 0; }
  html, body { width: 1200px; height: 795px; overflow: hidden; }
  body { background: var(--backdrop); position: relative; font-family: "Arimo", Arial, sans-serif; }

  /* Front of postcard */
  .card-front {
    position: absolute; left: 17px; top: 158px; width: 588px; height: 460px;
    background: var(--white); overflow: hidden;
  }
  .hero {
    position: absolute; inset: 0 0 138px 0;
    background: linear-gradient(115deg, #0a3f8f 0%, #1166c9 45%, #2a8fe0 70%, #0b3f8c 100%);
  }
  .hero-art {
    position: absolute; left: 0; top: 0; width: 250px; height: 300px;
    background: radial-gradient(ellipse at 40% 45%, rgba(235,240,248,.85) 0%, rgba(170,190,215,.55) 45%, rgba(20,80,160,0) 75%);
  }
  .hero-sweep {
    position: absolute; right: -40px; top: 40px; width: 360px; height: 300px;
    background: radial-gradient(ellipse at 70% 55%, rgba(170,225,255,.55) 0%, rgba(90,170,240,.2) 40%, rgba(0,0,0,0) 70%);
  }
  .headline {
    position: absolute; left: 0; right: 0; top: 36px; text-align: center;
    font-family: "Cinzel", serif; font-weight: 900; font-size: 46px; color: var(--white);
    letter-spacing: 1px; -webkit-text-stroke: 2px var(--royal); paint-order: stroke fill;
    text-shadow: 0 0 4px #0a3f8f;
  }
  .edition {
    position: absolute; left: 158px; top: 86px; width: 308px; height: 34px;
    background: rgba(10,45,105,.85); color: var(--white); text-align: center;
    font-family: "Gelasio", Georgia, serif; font-size: 27px; line-height: 34px;
  }
  .event-name {
    position: absolute; left: 0; right: 0; top: 122px; text-align: center;
    font-weight: 700; font-size: 23px; color: var(--white);
    -webkit-text-stroke: 2px var(--royal); paint-order: stroke fill;
  }
  .date-band {
    position: absolute; left: 130px; top: 176px; width: 400px; height: 34px;
    background: linear-gradient(90deg, rgba(10,40,100,0), rgba(10,40,100,.6) 20%, rgba(10,40,100,.6) 80%, rgba(10,40,100,0));
  }
  .event-date {
    position: absolute; left: 0; right: 0; top: 180px; text-align: center;
    font-family: "Cinzel", serif; font-weight: 700; font-size: 22px; color: var(--white);
    letter-spacing: .5px;
  }
  .venue-burst { position: absolute; left: 118px; top: 208px; width: 370px; height: 118px; }
  .venue {
    position: absolute; left: 118px; top: 236px; width: 370px; text-align: center;
    color: var(--white); font-size: 19px; line-height: 24px;
  }
  .contact-row {
    position: absolute; left: 0; right: 0; top: 300px; height: 24px;
    display: flex; justify-content: space-between; align-items: center; padding: 0 14px 0 10px;
    color: var(--white); font-weight: 700;
  }
  .contact { display: flex; align-items: center; gap: 6px; font-size: 15px; }
  .contact.email { font-size: 13px; letter-spacing: .3px; }
  .partners {
    position: absolute; left: 0; right: 0; top: 322px; height: 106px;
    background: linear-gradient(180deg, #e9eef3 0%, #ffffff 30%);
    display: flex; align-items: center; justify-content: space-around; padding: 0 30px;
  }
  .partner { display: flex; align-items: center; gap: 8px; color: var(--navy); font-family: "Gelasio", Georgia, serif; }
  .partner-mark { width: 62px; height: 62px; border-radius: 50%; border: 2px solid var(--navy); flex: none; }
  .partner-name { font-size: 14px; line-height: 17px; }
  .partner-name.lead { font-size: 17px; line-height: 20px; }
  .web-band {
    position: absolute; left: 0; right: 0; bottom: 0; height: 32px; background: var(--sky);
    color: var(--white); text-align: center; font-size: 17px; line-height: 32px;
  }

  /* Back of postcard */
  .card-back {
    position: absolute; left: 616px; top: 156px; width: 576px; height: 452px;
    background: linear-gradient(160deg, #e4ebf4 0%, #eef4fa 40%, #e2eef8 100%); overflow: hidden;
  }
  .back-art {
    position: absolute; left: 0; top: 0; width: 300px; height: 300px;
    background: radial-gradient(ellipse at 40% 40%, rgba(190,205,222,.9) 0%, rgba(210,222,236,.5) 45%, rgba(230,238,246,0) 75%);
  }
  .back-sweep {
    position: absolute; left: 0; right: 0; bottom: 20px; height: 180px;
    background: radial-gradient(ellipse at 30% 90%, rgba(255,255,255,.8) 0%, rgba(200,225,245,.35) 40%, rgba(0,0,0,0) 70%);
  }
  .divider { position: absolute; left: 339px; top: 0; width: 1px; height: 200px; background: rgba(255,255,255,.6); }
  .stamp-box { position: absolute; left: 415px; top: 39px; width: 123px; height: 74px; background: var(--stamp); }
  .address-line {
    position: absolute; height: 0; border-top: 3px dotted var(--dot); width: 210px;
  }
  .back-band { position: absolute; left: 0; right: 0; bottom: 0; height: 20px; background: #4fa6d6; }
</style>
</head>
<body>

<section class="card-front" aria-label="Postcard front">
  <div class="hero">
    <div class="hero-art" role="img" aria-label="Pale sketch of a human heart"></div>
    <div class="hero-sweep" role="img" aria-label="Soft light streaks"></div>
  </div>
  <h1 class="headline">Save the Date</h1>
  <div class="edition">The 12th Annual</div>
  <h2 class="event-name">Heartline Crew Colloquium</h2>
  <div class="date-band"></div>
  <p class="event-date">Friday, June 7, 2019</p>
  <svg class="venue-burst" viewBox="0 0 370 118" aria-hidden="true">
    <polygon fill="#0b4aa0" stroke="#5fb4f0" stroke-width="1.5"
      points="30,22 60,14 78,2 100,12 140,4 170,14 205,2 235,12 270,4 300,14 330,6 342,24 368,30 350,48 366,62 348,76 362,96 330,98 318,116 290,106 255,116 220,104 185,116 150,106 115,116 85,104 55,112 42,96 10,96 24,78 2,64 22,50 4,34"/>
  </svg>
  <p class="venue">The Varrick–Dunmore Building<br>318 West 57th Street | NYC</p>
  <div class="contact-row">
    <span class="contact phone">
      <svg width="26" height="18" viewBox="0 0 26 18" aria-hidden="true">
        <path fill="#fff" d="M2 6c0-3 5-5 11-5s11 2 11 5v2h-6V5c-2-.6-8-.6-10 0v3H2z"/>
        <rect x="5" y="9" width="16" height="8" rx="1.5" fill="#fff"/>
        <circle cx="13" cy="13" r="2.5" fill="#0b3f8c"/>
      </svg>
      212-555-0147
    </span>
    <span class="contact email">
      <svg width="28" height="16" viewBox="0 0 28 16" aria-hidden="true">
        <rect x="1" y="1" width="26" height="14" fill="#fff"/>
        <path d="M1 1l13 8 13-8" fill="none" stroke="#0b3f8c" stroke-width="1.5"/>
      </svg>
      ASK@QB-ZRH.ORG
    </span>
  </div>
  <div class="partners">
    <div class="partner"><span class="partner-mark"></span><span class="partner-name">Harbor Pulse<br>Society</span></div>
    <div class="partner"><span class="partner-mark"></span><span class="partner-name lead">Meridian Heart Guild<br>Eastern Chapter</span></div>
    <div class="partner"><span class="partner-mark"></span><span class="partner-name">Lindell Cardiac<br>Alliance</span></div>
  </div>
  <div class="web-band">www.qb-zrh.org/events</div>
</section>

<section class="card-back" aria-label="Postcard back">
  <div class="back-art" role="img" aria-label="Faint sketch of a human heart"></div>
  <div class="back-sweep" role="img" aria-label="Soft light streaks"></div>
  <div class="divider"></div>
  <div class="stamp-box" aria-label="Stamp area"></div>
  <div class="address-line" style="left:318px; top:267px;"></div>
  <div class="address-line" style="left:316px; top:296px;"></div>
  <div class="address-line" style="left:320px; top:330px;"></div>
  <div class="address-line" style="left:319px; top:361px;"></div>
  <div class="back-band"></div>
</section>

</body>
</html>
```